Flyer for American Indian Elders on Dementia Warning Signs

We need a flyer designed for older adults who are American Indian or Alaska Native (in the U.S.).

Ideally, the flyer should complement the colors of our logos. The project logo and our organization logo are attached to the brief.

When people see the flyer we want them to feel that it represents their culture, is warm, and professional but relatable to older adults and people who have limited incomes.

I have attached an earlier draft of the document we designed ourselves BUT we want different and better.

It is for older adults who have trouble reading so:
1. you must use a font that is 11.5 points or larger
2. Do not put text over complex pictures or use shading with words
3. You can use a serif font for the heading, but should use san serif for the body text
4. There should be good contrast between the font color and background

Please do not use any images that include a head dress or pictures of American Indian people or things that are very traditional or "token" imagery.

We need to save a small space under the call out box/ somewhere on the flyer for other people to add their logo once they download.

Let us know if you have questions or need additional information.

Target Market(s)

Older American Indian people

Font styles to use
Serif
Sans Serif

Requirements
Must have
• Easy to read for older adults
Should not have
• indian headdress

```html
<!DOCTYPE html>
<html lang="en">
<head>
<meta charset="utf-8">
<title>10 Warning Signs of Abnormal Memory Changes or Dementia</title>
<link href="https://fonts.googleapis.com/css2?family=Montserrat:wght@600;700&family=Oswald:wght@500&family=Roboto+Condensed:wght@400&family=Roboto:wght@400&family=Prata&display=swap" rel="stylesheet">
<style>
  :root {
    --teal: #65b3bc;
    --teal-dark: #4c9aa3;
    --rust: #b24c45;
    --rust-soft: #c0685f;
    --ink: #1f1f1f;
    --body: #2a2a2a;
    --brown: #9a706b;
    --box-grey: #ededed;
    --line: #9bbbbf;
    --paper: #ffffff;
  }
  * { box-sizing: border-box; margin: 0; padding: 0; }
  html, body { width: 1200px; height: 2400px; overflow: hidden; background: var(--paper); }
  .canvas { position: relative; width: 1200px; height: 2400px; }
  .flyer { position: absolute; left: 15px; top: 420px; width: 1170px; height: 1560px; }

  .count-badge {
    position: absolute; left: 28px; top: 73px; width: 176px; height: 176px;
    background: var(--teal); color: var(--paper);
    font-family: "Prata", Georgia, serif; font-size: 150px; line-height: 176px;
    text-align: center; letter-spacing: -8px;
  }
  .count-badge::after {
    content: ""; position: absolute; left: 14px; bottom: -10px;
    border-left: 10px solid transparent; border-right: 10px solid transparent;
    border-top: 10px solid var(--teal);
  }
  .title { position: absolute; left: 224px; top: 74px; font-family: "Montserrat", Arial, sans-serif; font-weight: 700; font-size: 37px; line-height: 42px; }
  .title .teal { color: var(--teal); }
  .title .ink { color: var(--ink); }
  .title .rust { color: var(--rust); }

  .timeline { position: absolute; left: 104px; top: 300px; width: 2px; height: 1250px; background: var(--line); }
  .timeline-dot { position: absolute; left: 98px; top: 1522px; width: 14px; height: 14px; border-radius: 50%; background: var(--teal-dark); }

  .sign { position: absolute; left: 0; width: 610px; }
  .sign-number {
    position: absolute; left: 68px; top: -8px; width: 74px; height: 72px;
    background: var(--box-grey); color: var(--teal);
    font-family: "Montserrat", Arial, sans-serif; font-weight: 600; font-size: 58px; line-height: 72px; text-align: center;
  }
  .sign-icon { position: absolute; left: 172px; top: -6px; width: 44px; height: 44px; }
  .sign-head {
    margin-left: 228px; font-family: "Oswald", "Arial Narrow", sans-serif; font-weight: 500;
    font-size: 20px; line-height: 28px; color: var(--rust); text-transform: uppercase;
  }
  .sign-head.soft { color: var(--rust-soft); }
  .sign-body { margin-left: 175px; margin-top: 8px; font-family: "Roboto Condensed", "Arial Narrow", sans-serif; font-size: 19px; line-height: 26px; color: var(--body); }
  .sign-body.plain { font-family: "Roboto", Arial, sans-serif; font-size: 19px; }
  .sign-body.small { font-size: 17px; line-height: 20px; margin-left: 168px; }

  .brain-visual {
    position: absolute; left: 662px; top: 7px; width: 503px; height: 600px;
    border-radius: 48% 20% 50% 50%;
    background: radial-gradient(circle at 42% 35%, #f0a040 0%, #e0502a 18%, #2c4fd0 45%, #1e7ee0 70%, #3cc0f0 100%);
    box-shadow: -16px 24px 0 -4px var(--teal-dark);
  }

  .partner { position: absolute; display: flex; align-items: center; gap: 12px; font-family: "Montserrat", Arial, sans-serif; font-weight: 700; color: var(--teal-dark); font-size: 22px; line-height: 26px; }
  .partner-mark { width: 52px; height: 52px; border-radius: 50%; background: var(--teal); flex: none; }
  .partner-a { left: 700px; top: 645px; }
  .partner-b { left: 700px; top: 745px; }
  .partner-b .partner-mark { border-radius: 0; }

  .callout {
    position: absolute; left: 704px; top: 826px; width: 395px; height: 532px;
    background: var(--teal); color: var(--paper); padding: 58px 30px 0;
    font-family: "Roboto Condensed", "Arial Narrow", sans-serif; font-size: 21px; line-height: 29px; text-align: center;
  }
  .callout p + p { margin-top: 30px; }
  .callout p.gap { margin-top: 58px; }
  .learn-more {
    position: absolute; left: 704px; top: 1358px; width: 395px; height: 196px;
    background: var(--brown); color: var(--paper); padding: 24px 20px 0;
    font-family: "Roboto Condensed", "Arial Narrow", sans-serif; font-size: 21px; line-height: 30px; text-align: center;
  }
</style>
</head>
<body>
<div class="canvas">
  <article class="flyer">
    <div class="count-badge">10</div>
    <h1 class="title">
      <span class="teal">WARNING SINGS</span><br>
      <span class="ink">OF ABNORMAL</span><br>
      <span class="rust">MEMORY CHANGES</span><br>
      <span class="ink">OR DEMENTIA</span>
    </h1>

    <div class="timeline"></div>
    <div class="timeline-dot"></div>

    <section class="sign" style="top:322px">
      <div class="sign-number">1</div>
      <svg class="sign-icon" viewBox="0 0 44 44" fill="none" stroke="#b24c45" stroke-width="2"><circle cx="20" cy="24" r="16"/><circle cx="34" cy="10" r="7"/></svg>
      <h2 class="sign-head">Memory loss that affectsyour daily life</h2>
      <p class="sign-body">You may Forget events or important dates Repeat yourself&nbsp; Rely more often on lists or sticky notes to remember things</p>
    </section>

    <section class="sign" style="top:448px">
      <div class="sign-number">2</div>
      <svg class="sign-icon" viewBox="0 0 44 44" fill="none" stroke="#b24c45" stroke-width="2"><circle cx="20" cy="22" r="15"/><path d="M20 22 L20 7 M20 22 L33 28"/></svg>
      <h2 class="sign-head">Trouble planning or&nbsp; solving problems</h2>
      <p class="sign-body">You may have a harder time: Paying bills Cooking recipes you have used&nbsp; for years</p>
    </section>

    <section class="sign" style="top:557px">
      <div class="sign-number">3</div>
      <svg class="sign-icon" viewBox="0 0 44 44" fill="none" stroke="#b24c45" stroke-width="2"><circle cx="22" cy="22" r="15"/><path d="M22 12 V22 L29 26"/></svg>
      <h2 class="sign-head">Get confused about the time, date, or<br>where you are.</h2>
    </section>

    <section class="sign" style="top:637px">
      <div class="sign-number">4</div>
      <svg class="sign-icon" viewBox="0 0 44 44" fill="none" stroke="#b24c45" stroke-width="2"><rect x="8" y="8" width="26" height="30"/><path d="M14 22 L20 28 L34 10"/></svg>
      <h2 class="sign-head">Daily tasks are&nbsp; getting harder</h2>
      <p class="sign-body">including Driving Making a grocery list&nbsp; or going shopping</p>
    </section>

    <section class="sign" style="top:717px">
      <div class="sign-number" style="top:12px">5</div>
      <svg class="sign-icon" viewBox="0 0 44 44" fill="none" stroke="#b24c45" stroke-width="2"><circle cx="28" cy="14" r="8"/><path d="M6 40 C6 20 14 14 22 22"/></svg>
      <h2 class="sign-head">Troublewith how your eyesight and<br>thinking work together&nbsp; that<br>&nbsp; gets worse</h2>
      <p class="sign-body plain">This includesTripping, falls, or problems with your balance Spilling or dropping things more</p>
    </section>

    <section class="sign" style="top:885px">
      <div class="sign-number">6</div>
      <svg class="sign-icon" viewBox="0 0 44 44" fill="none" stroke="#b24c45" stroke-width="2"><path d="M4 10 H24 M4 18 H22 M4 26 H18 M4 34 H16 M28 36 L38 8"/></svg>
      <h2 class="sign-head" style="margin-left:240px">New troubletalking or writing</h2>
      <p class="sign-body">You have a hard time finding the words you want to say. For example, you may say “that thing on your wrist that tells time” instead of “watch.”</p>
    </section>

    <section class="sign" style="top:1019px">
      <div class="sign-number">7</div>
      <svg class="sign-icon" viewBox="0 0 44 44" fill="none" stroke="#b24c45" stroke-width="2"><circle cx="14" cy="14" r="6"/><circle cx="30" cy="32" r="6"/></svg>
      <h2 class="sign-head soft" style="margin-left:240px">Loseand cannot find things</h2>
      <p class="sign-body">For example, you Can’t find the coffee pot that you use every day Mightput your car keys in the freezer</p>
    </section>

    <section class="sign" style="top:1127px">
      <div class="sign-number" style="top:12px">8</div>
      <svg class="sign-icon" viewBox="0 0 44 44" fill="none" stroke="#b24c45" stroke-width="2"><circle cx="22" cy="16" r="9"/><path d="M10 40 C10 28 34 28 34 40"/></svg>
      <h2 class="sign-head">Notice changes&nbsp; in your<br>mood or personality</h2>
      <p class="sign-body">such as being Easily mad or sad in everyday&nbsp; situtions More fearful&nbsp; (scared) or suspicious (not trusting)</p>
    </section>

    <section class="sign" style="top:1268px">
      <div class="sign-number" style="top:4px">9</div>
      <svg class="sign-icon" viewBox="0 0 44 44" fill="none" stroke="#b24c45" stroke-width="2"><circle cx="22" cy="12" r="7"/><path d="M8 38 L22 24 L36 38 Z"/></svg>
      <h2 class="sign-head" style="margin-left:220px">Make poorchoices.this&nbsp; may<br>make you more likely to</h2>
      <p class="sign-body" style="margin-left:168px">Spend money you do not have or be a scam victim Stop washing up regularly or pay less attention to how you look Forget to take care of your pet</p>
    </section>

    <section class="sign" style="top:1430px">
      <div class="sign-number" style="top:12px">10</div>
      <svg class="sign-icon" viewBox="0 0 44 44" fill="none" stroke="#b24c45" stroke-width="2"><circle cx="14" cy="14" r="6"/><circle cx="30" cy="14" r="6"/><path d="M4 36 C8 26 36 26 40 36"/></svg>
      <h2 class="sign-head">Pull away from friends and family<br>because&nbsp; it is harder to keep up</h2>
      <p class="sign-body small">You may not want to do things you used to enjoy, like sporting events, church, music, or sex.</p>
    </section>

    <div class="brain-visual" role="img" aria-label="Illustration of a human head in profile showing the brain glowing orange inside a blue outline, framed by teal leaf shapes"></div>

    <div class="partner partner-a"><span class="partner-mark"></span><span>ELDERS BRAIN<br>WELLNESS CENTER</span></div>
    <div class="partner partner-b"><span class="partner-mark"></span><span>COUNCIL ON<br>NATIVE ELDER CARE</span></div>

    <div class="callout">
      <p>American Indian and Alaska Native people have a higher risk of dementia. than White people.</p>
      <p class="gap">Big changes in memory or thinking that make it hard to get through the day are not a normal part of aging.</p>
      <p>People with one or more of these 10 signs should talk to their doctor to find the cause. It is not always dementia.</p>
      <p>Early dementia diagnosis gives you a chance to get care and plan your future.</p>
    </div>
    <div class="learn-more">
      <p>To learn more about the warning signs of de-mentia in American Indian and Alaska Native people, visit:<br>www.elderbrainwellness.org<br>www.healthyagingnow.org</p>
    </div>
  </article>
</div>
</body>
</html>
```